Veltra Homes Real Estate Brokerage Recruiting Flyer

We are a real estate brokerage looking to hire more real estate agents. We need to list everything we have to offer as a company so real estate agents will join our company. this is our company website: www.Veltrahomes.example .

100% COMMISSION NO MONTHLY FEE
$450 Flat Transaction FEE

What We Offer:
24/7 Office Access
Free E & O Insurance for 1st Year
Free Online CE and PLE
Free 1,000 Business Cards
Free Professional Social Media Marketing
Free Printing, Scanning, and Copies
Free Buyer and Seller Presentation Packages
Free Papervane Cloud Based Document Management Access
Access to our Internal Brokerage Forum
Company Profit Sharing!
Private Offices Available to Rent

*Lead Generation Software with over 3,000 Leads
*10 Leads to Start
* Free Personal CRM and Website
*Restrictions and Rules apply

Company Address:
4817 Marlow Creek Road
Suite 412
Fairfax, VA 22147
Phone: 703-241-7086
email: info@veltrahomes.example

Target Market(s)

Real Estate Agents

Industry/Entity Type

Real Estate

Colors
0555a3
ffffff

Requirements
Must have
• 100% COMMISSION NO MONTHLY FEE
$450 Flat Transaction FEE

What We Offer:
24/7 Office Access
Free Online CE and PLE
Free 1,000 Business Cards
Company Profit Sharing!

*10 Leads to Start

Company Address:
4817 Marlow Creek Road
Suite 412
Fairfax, VA 22147
Phone: 703-241-7086

```html
<!DOCTYPE html>
<html lang="en">
<head>
<meta charset="utf-8">
<title>Veltra Homes – Agent Recruiting Flyer</title>
<link rel="stylesheet" href="https://fonts.googleapis.com/css2?family=Montserrat:wght@500;600;700;800;900&family=Oswald:wght@400;500;600&display=swap">
<style>
  :root {
    --brand-blue: #0555a3;
    --mid-blue: #1e66bd;
    --light-blue: #3f86d6;
    --deep-blue: #0a3f86;
    --title-blue: #0f4fa8;
    --orange: #f7931e;
    --white: #ffffff;
    --footer-grey: #e4e6ea;
    --stage: #dcdad6;
  }
  * { box-sizing: border-box; margin: 0; padding: 0; }
  html, body { width: 1200px; height: 979px; overflow: hidden; }
  body { background: var(--stage); position: relative; font-family: "Montserrat", sans-serif; }

  .flyer {
    position: absolute; left: 255px; top: 20px;
    width: 690px; height: 939px;
    background: var(--white); overflow: hidden;
    box-shadow: 0 2px 10px rgba(0,0,0,.15);
  }

  .hero-photo {
    position: absolute; left: 0; top: 0; width: 690px; height: 310px;
    background: linear-gradient(180deg, #ffffff 0%, #f4eef3 22%, #e8c9d2 45%, #8a8fb4 72%, #3c5f9a 100%);
  }

  .headline {
    position: absolute; left: 0; top: 22px; width: 690px; text-align: center;
    color: var(--title-blue);
  }
  .headline__main { font-weight: 900; font-size: 36px; letter-spacing: -0.5px; line-height: 38px; }
  .headline__sub { font-weight: 500; font-size: 21px; color: #1f3b6e; margin-top: 4px; letter-spacing: .3px; }

  .bands { position: absolute; left: 0; top: 290px; width: 690px; height: 170px; }

  .fee-block {
    position: absolute; left: 0; top: 325px; width: 300px; text-align: center;
    font-family: "Oswald", sans-serif; color: var(--white); font-weight: 500;
  }
  .fee-block__note { font-size: 18px; line-height: 22px; letter-spacing: .4px; }
  .fee-block__price { font-size: 28px; line-height: 27px; margin-top: 10px; font-weight: 600; }

  .leads-block {
    position: absolute; left: 336px; top: 295px; width: 330px; color: var(--white);
  }
  .leads-block__title {
    font-family: "Oswald", sans-serif; font-weight: 500; font-size: 24px; line-height: 29px; letter-spacing: .3px;
  }
  .leads-block__title span { display: block; }
  .leads-block__title span:first-child { padding-left: 6px; }
  .leads-block__rule { width: 290px; height: 2px; background: var(--white); margin: 10px 0 9px 7px; }
  .leads-block__list { list-style: none; font-weight: 700; font-size: 13.5px; line-height: 21px; }
  .leads-block__list li:first-child { padding-left: 4px; }

  .perks-column {
    position: absolute; left: 0; top: 419px; width: 212px; height: 424px;
    background: linear-gradient(170deg, var(--mid-blue) 0%, #2a72c6 55%, #4e8fd6 100%);
    color: var(--white);
  }
  .perks-column__commission { position: absolute; left: 30px; top: 52px; font-family: "Oswald", sans-serif; font-weight: 600; }
  .perks-column__pct { font-size: 62px; line-height: 62px; }
  .perks-column__word { font-size: 30px; line-height: 34px; letter-spacing: .5px; }
  .perks-column__nofee {
    position: absolute; left: 36px; top: 182px;
    font-family: "Oswald", sans-serif; font-weight: 600; font-size: 39px; line-height: 42px;
  }
  .perks-column__license {
    position: absolute; left: 37px; top: 325px; font-size: 11.5px; line-height: 16.5px; font-weight: 500;
  }

  .offer { position: absolute; left: 239px; top: 452px; }
  .offer__title { font-weight: 900; font-size: 34px; color: var(--orange); letter-spacing: -0.3px; line-height: 40px; }
  .offer__list { list-style: none; margin-top: 2px; }
  .offer__item {
    display: flex; align-items: center; height: 30.2px;
    font-family: "Oswald", sans-serif; font-weight: 500; font-size: 15.5px; color: var(--mid-blue); letter-spacing: .1px;
  }
  .offer__tick { width: 15px; height: 15px; margin: 0 11px 0 7px; flex: none; }

  .footer {
    position: absolute; left: 0; top: 843px; width: 690px; height: 96px; background: var(--footer-grey);
  }
  .footer__brand {
    position: absolute; left: 28px; top: 33px;
    font-weight: 600; font-size: 22px; color: #4a6590; letter-spacing: .5px;
  }
  .footer__address {
    position: absolute; left: 250px; top: 34px; display: flex; gap: 10px;
    font-weight: 700; font-size: 11px; line-height: 15.5px; color: var(--mid-blue);
  }
  .footer__contact {
    position: absolute; left: 478px; top: 29px; font-weight: 700; font-size: 12px; color: var(--mid-blue);
  }
  .footer__row { display: flex; align-items: center; gap: 10px; height: 25px; white-space: nowrap; }
  .footer__icon { width: 16px; height: 16px; flex: none; }
</style>
</head>
<body>
  <main class="flyer">
    <div class="hero-photo" role="img" aria-label="Silhouettes of business people shaking hands over a city skyline at sunrise"></div>

    <header class="headline">
      <h1 class="headline__main">JOIN OUR WINNING TEAM</h1>
      <p class="headline__sub">OF AGENTS TODAY!</p>
    </header>

    <svg class="bands" viewBox="0 290 690 170" aria-hidden="true">
      <defs>
        <linearGradient id="leadsFill" x1="0" y1="0" x2="1" y2="1">
          <stop offset="0" stop-color="#0d4fa3"/>
          <stop offset="1" stop-color="#2a72c8"/>
        </linearGradient>
      </defs>
      <polygon points="0,308 314,308 294,419 0,419" fill="var(--orange)"/>
      <polygon points="315,295 690,295 690,456 288,456" fill="url(#leadsFill)"/>
      <polygon points="260,419 294,419 288,456" fill="var(--deep-blue)"/>
    </svg>

    <section class="fee-block">
      <p class="fee-block__note">RESTRICTIONS AND RULES APPLY</p>
      <p class="fee-block__price">$450 FLAT<br>TRANSACTION FEE</p>
    </section>

    <section class="leads-block">
      <h2 class="leads-block__title"><span>LEAD GENERATION SOFTWARE</span><span>WITH OVER 3,000 LEADS</span></h2>
      <div class="leads-block__rule"></div>
      <ul class="leads-block__list">
        <li>- 10 LEADS TO START</li>
        <li>- FREE PERSONAL CRM AND WEBSITE</li>
      </ul>
    </section>

    <aside class="perks-column" role="img" aria-label="Faint photo of smiling real estate agents behind blue overlay">
      <div class="perks-column__commission">
        <div class="perks-column__pct">100%</div>
        <div class="perks-column__word">COMMISSION</div>
      </div>
      <div class="perks-column__nofee">NO<br>MONTHLY<br>FEE</div>
      <p class="perks-column__license">LICENSED IN<br>D.C., MARYLAND,<br>AND VIRGINIA</p>
    </aside>

    <section class="offer">
      <h2 class="offer__title">WHAT WE OFFER</h2>
      <ul class="offer__list">
        <li class="offer__item"><svg class="offer__tick" viewBox="0 0 16 16"><rect x="1" y="2" width="12" height="12" fill="none" stroke="currentColor" stroke-width="1.4"/><path d="M4 7.5l3 3 8-8" fill="none" stroke="currentColor" stroke-width="1.6"/></svg>24/7 OFFICE ACCESS</li>
        <li class="offer__item"><svg class="offer__tick" viewBox="0 0 16 16"><rect x="1" y="2" width="12" height="12" fill="none" stroke="currentColor" stroke-width="1.4"/><path d="M4 7.5l3 3 8-8" fill="none" stroke="currentColor" stroke-width="1.6"/></svg>FREE E &amp; O INSURANCE FOR 1ST YEAR</li>
        <li class="offer__item"><svg class="offer__tick" viewBox="0 0 16 16"><rect x="1" y="2" width="12" height="12" fill="none" stroke="currentColor" stroke-width="1.4"/><path d="M4 7.5l3 3 8-8" fill="none" stroke="currentColor" stroke-width="1.6"/></svg>FREE ONLINE CE AND PLE</li>
        <li class="offer__item"><svg class="offer__tick" viewBox="0 0 16 16"><rect x="1" y="2" width="12" height="12" fill="none" stroke="currentColor" stroke-width="1.4"/><path d="M4 7.5l3 3 8-8" fill="none" stroke="currentColor" stroke-width="1.6"/></svg>FREE 1,000 BUSINESS CARDS</li>
        <li class="offer__item"><svg class="offer__tick" viewBox="0 0 16 16"><rect x="1" y="2" width="12" height="12" fill="none" stroke="currentColor" stroke-width="1.4"/><path d="M4 7.5l3 3 8-8" fill="none" stroke="currentColor" stroke-width="1.6"/></svg>FREE PROFESSIONAL SOCIAL MEDIA MARKETING</li>
        <li class="offer__item"><svg class="offer__tick" viewBox="0 0 16 16"><rect x="1" y="2" width="12" height="12" fill="none" stroke="currentColor" stroke-width="1.4"/><path d="M4 7.5l3 3 8-8" fill="none" stroke="currentColor" stroke-width="1.6"/></svg>FREE PRINTING, SCANNING, AND COPIES</li>
        <li class="offer__item"><svg class="offer__tick" viewBox="0 0 16 16"><rect x="1" y="2" width="12" height="12" fill="none" stroke="currentColor" stroke-width="1.4"/><path d="M4 7.5l3 3 8-8" fill="none" stroke="currentColor" stroke-width="1.6"/></svg>FREE BUYER AND SELLER PRESENTATION PACKAGES</li>
        <li class="offer__item"><svg class="offer__tick" viewBox="0 0 16 16"><rect x="1" y="2" width="12" height="12" fill="none" stroke="currentColor" stroke-width="1.4"/><path d="M4 7.5l3 3 8-8" fill="none" stroke="currentColor" stroke-width="1.6"/></svg>FREE PAPERVANE CLOUD BASED DOCUMENT MANAGEMENT ACCESS</li>
        <li class="offer__item"><svg class="offer__tick" viewBox="0 0 16 16"><rect x="1" y="2" width="12" height="12" fill="none" stroke="currentColor" stroke-width="1.4"/><path d="M4 7.5l3 3 8-8" fill="none" stroke="currentColor" stroke-width="1.6"/></svg>ACCESS TO OUR INTERNAL BROKERAGE FORUM</li>
        <li class="offer__item"><svg class="offer__tick" viewBox="0 0 16 16"><rect x="1" y="2" width="12" height="12" fill="none" stroke="currentColor" stroke-width="1.4"/><path d="M4 7.5l3 3 8-8" fill="none" stroke="currentColor" stroke-width="1.6"/></svg>COMPANY PROFIT SHARING!</li>
        <li class="offer__item"><svg class="offer__tick" viewBox="0 0 16 16"><rect x="1" y="2" width="12" height="12" fill="none" stroke="currentColor" stroke-width="1.4"/><path d="M4 7.5l3 3 8-8" fill="none" stroke="currentColor" stroke-width="1.6"/></svg>PRIVATE OFFICES AVAILABLE TO RENT</li>
      </ul>
    </section>

    <footer class="footer">
      <div class="footer__brand">Veltra Homes</div>
      <div class="footer__address">
        <svg class="footer__icon" viewBox="0 0 16 16"><path d="M8 1a5 5 0 0 0-5 5c0 4 5 9 5 9s5-5 5-9a5 5 0 0 0-5-5z" fill="var(--mid-blue)"/><circle cx="8" cy="6" r="1.8" fill="var(--footer-grey)"/></svg>
        <p>4817 MARLOW CREEK ROAD,<br>SUITE 412, FAIRFAX, VA 22147</p>
      </div>
      <div class="footer__contact">
        <div class="footer__row">
          <svg class="footer__icon" viewBox="0 0 16 16"><path d="M4 1l3 3-1.5 2a9 9 0 0 0 4.5 4.5L12 9l3 3-2 3C7 14 2 9 1 3z" fill="var(--mid-blue)"/></svg>
          <span>703-241-7086</span>
        </div>
        <div class="footer__row">
          <svg class="footer__icon" viewBox="0 0 16 16"><rect x="1" y="3" width="14" height="10" fill="var(--mid-blue)"/><path d="M1 3l7 6 7-6" fill="none" stroke="var(--footer-grey)" stroke-width="1.3"/></svg>
          <span>info@veltrahomes.example</span>
        </div>
      </div>
    </footer>
  </main>
</body>
</html>
```